BrightQuarry - IT Consultancy Website

Our company is called BrightQuarry and our purpose is to help companies sustainably embrace and reap the benefits of cloud platforms, through transforming practices, skills and technology using DevOps and Security practices such that they are able to automate, manage and secure their cloud platforms to deliver product to market with increasing velocity.

To get our business started I require a website that will model the typical layout of an IT consultancy services company to an Australian Market. There are many examples of such a site, here are some of them. We would like a landing page and then a few simple menu options (About, Blog, Services etc..) to additional content

http://kelvaro.com.au/
http://www.wembrith.com.au/
http://www.tazu.com.au/

I require the site to be created with a separate CSS file that maintains the colour palette. This is a very important requirement, I want to be able to change the colours employed in the site in a single location and not have to scan through multiple files to replace the codes.

The website must be built using static content as it will not be hosted on a web server but instead in NXC using V9 and Nimbex CDN. Therefore please stick to HTML, JavaScript, CSS and other static file formats. The website needs to be response, smooth and reactive. It should render on desktop, mobile and tablet and feature smooth scrolling, transitions and fade in's.

The website should give the customer confidence that they are dealing with a highly professional IT services company, focused strongly on cloud (NXC, Palvex Ostria, Tobrin Vault etc..), motivated by beautiful and fluid design.

In order to make this simpler for you, the designer, I have already purchased this template from https://themestallex.com/theme/the-harbor-multipurpose-template-QX7T49310 and uploaded it. Feel free to use this template if you choose (note that it makes use of a separate color palette which is a key requirement) or use one of your own choosing. If you do use this template ensure that it does not look too much like "another bootstrap site" therefore use the layout and widgets but make the site look fresh and original too.
Obviously you must delete all trace of the bootstrap package once the project has completed if you do use it

Target Market(s)

Corporate and medium enterprise businesses

Industry/Entity Type

Information Technology

Coding

Coded - Design and coding required

Number of Pages Required

4 page

Font styles to use
Sans Serif

Colors
abd036
33a6d7

Requirements
Must have
• The website should give the customer confidence that they are dealing with a highly professional IT services company, focused strongly on cloud (NXC, Palvex Ostria, Tobrin Vault etc..), motivated by beautiful and fluid design. Our company name is BrightQuarry, the site needs to pay homage to the themes of fluidity and logic
• Along with About Us, Services and a Blog page could I also get social logo's included too
Nice to have
• The website must be built using static content as it will not be hosted on a web server but instead in NXC using V9 and Nimbex CDN. Therefore please stick to HTML, JavaScript, CSS and other static file formats. The website needs to be response, smooth and reactive. It should render on desktop, mobile and tablet and feature smooth scrolling, transitions and fade in's.
Should not have
• Lurid colours, or too much animations. The design must "flow"

```html
<!DOCTYPE html>
<html lang="en">
<head>
<meta charset="utf-8">
<title>BrightQuarry – Cloud Consultancy</title>
<link rel="stylesheet" href="https://fonts.googleapis.com/css2?family=Raleway:wght@500;600;700&family=Lato:wght@400;700&display=swap">
<style>
:root{
  --blue:#33a6d7;
  --green:#abd036;
  --sky:#08a8ea;
  --ink:#222;
  --text:#333;
  --band:#f2f2f2;
  --footer:#333333;
  --footer-text:#e4e4e4;
  --white:#fff;
}
*{box-sizing:border-box;margin:0;padding:0}
html,body{width:1200px;height:2375px;overflow:hidden}
body{font-family:'Lato',sans-serif;color:var(--text);background:var(--white)}
h1,h2,h3,h4,.nav a,.btn-pill{font-family:'Raleway',sans-serif}
.wrap{position:relative;width:1200px}

.topbar{height:35px;background:var(--blue);display:flex;align-items:center;justify-content:space-between;padding:0 98px;color:var(--white);font-size:14px;font-weight:700}
.topbar .socials{display:flex;gap:10px}
.topbar .socials span{width:11px;height:11px;border-radius:50%;background:var(--white);display:block}
.topbar .contacts{display:flex;gap:28px;align-items:center}
.topbar .contacts div{display:flex;gap:7px;align-items:center}

.header{height:93px;display:flex;align-items:center;justify-content:space-between;padding:0 98px}
.brand{font-family:'Raleway',sans-serif;font-weight:700;font-size:22px;color:var(--green);display:flex;align-items:center;gap:10px}
.brand i{width:30px;height:30px;border:3px solid var(--blue);border-radius:50%;display:block}
.nav{display:flex;gap:0}
.nav a{font-size:16px;font-weight:700;color:var(--ink);text-decoration:none;margin-left:62px}
.nav a.active{color:var(--green)}

.hero{position:relative;height:513px;background:var(--sky);overflow:hidden}
.hero .art{position:absolute;inset:0;background:linear-gradient(180deg,#0aa9ec 0%,#0aa9ec 55%,#3fb7ef 100%)}
.hero h1{position:absolute;right:101px;top:320px;text-align:right;color:var(--white);font-size:25px;line-height:36px;font-weight:700}
.hero .arrow{position:absolute;top:364px;width:46px;height:42px;background:var(--green);display:flex;align-items:center;justify-content:center}
.hero .arrow.left{left:0;border-radius:0 21px 21px 0}
.hero .arrow.right{right:0;border-radius:21px 0 0 21px}

.cta{height:87px;background:var(--band);display:flex;align-items:center;justify-content:space-between;padding:0 100px 0 98px}
.cta p{font-family:'Raleway',sans-serif;font-weight:700;font-size:23px;color:var(--ink)}
.btn-pill{width:185px;height:42px;border-radius:21px;background:var(--blue);color:var(--white);font-weight:700;font-size:18px;display:flex;align-items:center;justify-content:center}

.section-title{text-align:center;font-size:27px;font-weight:700;color:var(--blue)}
.section-title span{color:var(--green)}
.divider{display:flex;align-items:center;justify-content:center;gap:8px;margin:14px auto 0}
.divider b{display:block;width:110px;height:1px;background:#ccc}
.divider i{width:12px;height:12px;border:2px solid var(--blue);border-radius:50%;display:block}
.btn-line{display:inline-flex;align-items:center;justify-content:center;width:98px;height:28px;border:1px solid var(--green);border-radius:14px;color:var(--green);font-size:13px}

.services{height:492px;padding-top:42px}
.services .lead{width:700px;margin:22px auto 0;text-align:center;font-size:15px;line-height:22px;color:var(--ink)}
.service-grid{position:relative;height:290px;margin-top:36px}
.service{position:absolute;top:20px;width:240px;text-align:center}
.service .icon{width:60px;height:60px;border-radius:50%;background:var(--blue);margin:0 auto;display:flex;align-items:center;justify-content:center}
.service h3{margin-top:18px;font-size:17px;font-weight:600;color:var(--green)}
.service p{margin-top:8px;font-size:13.5px;line-height:19px;color:var(--ink)}
.service .btn-line{margin-top:18px}
.vrule{position:absolute;top:0;width:1px;height:270px;background:#e6e6e6}

.welcome{height:308px;background:var(--band);padding-top:40px;text-align:center}
.welcome p{width:970px;margin:20px auto 0;font-size:13.5px;line-height:22px;color:var(--ink)}
.welcome .btn-line{margin-top:22px}

.blog{position:relative;height:456px;padding-top:42px}
.post{position:absolute;top:155px;width:290px;text-align:center}
.post .thumb{position:relative;width:132px;height:132px;border-radius:50%;margin:0 auto;overflow:hidden}
.post .thumb .date{position:absolute;left:0;right:0;bottom:0;height:52px;background:rgba(51,166,215,.85);color:var(--white);font-size:13px;font-weight:700;padding-top:8px}
.post h3{margin-top:22px;font-size:16.5px;font-weight:600;color:var(--green)}
.post p{margin-top:8px;font-size:13.5px;line-height:21px;color:var(--ink)}
.post p em{font-style:normal;color:var(--blue)}

.footer{height:261px;background:var(--footer);color:var(--footer-text);position:relative}
.footer h4{font-size:15px;font-weight:700;color:var(--white);padding-bottom:12px;border-bottom:1px solid #4a4a4a}
.fcol{position:absolute;top:28px}
.quick ul{list-style:none;margin-top:20px}
.quick li{font-size:13.5px;line-height:34px;display:flex;align-items:center;gap:10px}
.quick li::before{content:"";width:6px;height:6px;border:1.5px solid var(--green);border-radius:50%}
.contact .row{display:flex;gap:12px;font-size:13.5px;line-height:19px;margin-top:20px}
.contact .row svg{flex:none;margin-top:2px}
.form .field{width:256px;height:26px;border:1px solid #666;border-radius:13px;margin-top:12px;padding:4px 16px;font-size:13px;color:var(--white)}
.form .field.msg{height:42px}
.form .send{margin-top:10px;width:86px;height:28px;border:1px solid var(--green);border-radius:14px;color:var(--green);font-weight:700;font-size:15px;display:flex;align-items:center;justify-content:center;font-family:'Raleway',sans-serif}
.flogo{position:absolute;left:883px;top:72px;width:217px;text-align:center;font-family:'Raleway',sans-serif;font-size:28px;font-weight:600;color:#8a8a8a}
.fsocial{position:absolute;left:900px;top:192px;display:flex;gap:14px}
.fsocial span{width:37px;height:37px;border-radius:50%;border:1.5px solid var(--blue)}
.fsocial span:last-child{border-color:#e8782d}
.copy{height:43px;background:var(--blue);color:var(--white);font-size:13px;display:flex;align-items:center;justify-content:center;font-family:'Raleway',sans-serif}
</style>
</head>
<body>
<div class="wrap">

<div class="topbar">
  <div class="socials"><span></span><span></span><span></span><span></span></div>
  <div class="contacts">
    <div><svg width="14" height="14" viewBox="0 0 24 24"><path fill="#fff" d="M6.6 10.8a15 15 0 0 0 6.6 6.6l2.2-2.2c.3-.3.7-.4 1-.2 1.1.4 2.3.6 3.6.6.6 0 1 .4 1 1V20c0 .6-.4 1-1 1A17 17 0 0 1 3 4c0-.6.4-1 1-1h3.5c.6 0 1 .4 1 1 0 1.3.2 2.5.6 3.6.1.3 0 .7-.2 1z"/></svg>555-014-2290</div>
    <div><svg width="16" height="12" viewBox="0 0 16 12"><rect x="0.5" y="0.5" width="15" height="11" fill="none" stroke="#fff"/><path d="M1 1l7 6 7-6" fill="none" stroke="#fff"/></svg>info@brightquarry.com</div>
  </div>
</div>

<header class="header">
  <div class="brand"><i></i>BrightQuarry</div>
  <nav class="nav">
    <a class="active">Home</a><a>About Us</a><a>Services</a><a>Blog</a><a>Contact Us</a>
  </nav>
</header>

<section class="hero">
  <div class="art" role="img" aria-label="Flat illustration of a light bulb glowing over green trees and a city skyline with clouds on a blue sky"></div>
  <div class="arrow left"><svg width="18" height="16" viewBox="0 0 18 16"><path d="M9 2L3 8l6 6M15 2L9 8l6 6" fill="none" stroke="#fff" stroke-width="2"/></svg></div>
  <div class="arrow right"><svg width="18" height="16" viewBox="0 0 18 16"><path d="M3 2l6 6-6 6M9 2l6 6-6 6" fill="none" stroke="#fff" stroke-width="2"/></svg></div>
  <h1>Our Aim Is To Help Companies<br>Sustainably Embrace &amp; Reap The<br>Benefits Of Cloud Platforms</h1>
</section>

<div class="cta">
  <p>Lorem ipsum dolor sit amet consectetuer adipiscing elit sed diam</p>
  <div class="btn-pill">Learn More</div>
</div>

<section class="services">
  <h2 class="section-title">Our <span>Services</span></h2>
  <div class="divider"><b></b><i></i><b></b></div>
  <p class="lead">Lorem ipsum dolor sit amet consectetuer adipiscing elit sed diam nonummy nibh euismod tincidunt ut laoreet dolore magna aliquam erat volutpat.</p>
  <div class="service-grid">
    <div class="vrule" style="left:451px"></div>
    <div class="vrule" style="left:747px"></div>
    <div class="service" style="left:182px">
      <div class="icon"><svg width="34" height="22" viewBox="0 0 34 22"><path d="M9 21a7 7 0 0 1 0-14 9 9 0 0 1 17 2 6 6 0 0 1-1 12z" fill="#fff"/></svg></div>
      <h3>NXC</h3>
      <p>Lorem ipsum dolor sit amet consec<br>tetuer adipiscing elit sed diam<br>mmy nibh euismod</p>
      <span class="btn-line">Read More</span>
    </div>
    <div class="service" style="left:480px">
      <div class="icon"><svg width="34" height="22" viewBox="0 0 34 22"><path d="M9 21a7 7 0 0 1 0-14 9 9 0 0 1 17 2 6 6 0 0 1-1 12z" fill="none" stroke="#fff" stroke-width="2"/></svg></div>
      <h3>Palvex Ostria</h3>
      <p>Lorem ipsum dolor sit amet consec<br>tetuer adipiscing elit sed diam<br>mmy nibh euismod</p>
      <span class="btn-line">Read More</span>
    </div>
    <div class="service" style="left:776px">
      <div class="icon"><svg width="34" height="22" viewBox="0 0 34 22"><path d="M9 21a7 7 0 0 1 0-14 9 9 0 0 1 17 2 6 6 0 0 1-1 12z" fill="none" stroke="#fff" stroke-width="2"/></svg></div>
      <h3>Tobrin Vault</h3>
      <p>Lorem ipsum dolor sit amet consec<br>tetuer adipiscing elit sed diam<br>mmy nibh euismod</p>
      <span class="btn-line">Read More</span>
    </div>
  </div>
</section>

<section class="welcome">
  <h2 class="section-title">Welcome to <span>BrightQuarry</span></h2>
  <div class="divider"><b></b><i></i><b></b></div>
  <p>Lorem ipsum dolor sit amet, consectetuer adipiscing elit, sed diam nonummy nibh euismod tincidunt ut laoreet dolore magna aliquam erat volutpat. Ut wisi enim ad minim veniam, quis nostrud exerci tation ullamcorper suscipit lobortis nisl ut aliquip ex ea commodo consequat. Duis autem vel eum iriure dolor in hendrerit in vulputate velit esse molestie consequat, vel illum dolore eu feugiat nulla facilisis at vero eros et accumsan et iusto odio dignissim qui blandit praesent luptatum zzril delenit augue duis dolore te feugait nulla facilisi.</p>
  <span class="btn-line">Read More</span>
</section>

<section class="blog">
  <h2 class="section-title">Blog <span>Posts</span></h2>
  <div class="divider"><b></b><i></i><b></b></div>
  <article class="post" style="left:103px">
    <div class="thumb" role="img" aria-label="Illustration of a cloud surrounded by app and message icons" style="background:linear-gradient(160deg,#e9f3fa,#5fb8e6)"><div class="date">05.Aug.2016</div></div>
    <h3>Lorem ipsum dolor sit amet</h3>
    <p>Lorem ipsum dolor sit amet, consectetuer adipiscing elit, sed diam nonummy nibh euismod tincidunt ut laoreet dolore magna aliquam erat volutpat. Ut wisi enim ad minim...<em>[+]</em></p>
  </article>
  <article class="post" style="left:453px">
    <div class="thumb" role="img" aria-label="Photo of glowing network lights over a dark blue background" style="background:linear-gradient(160deg,#0d4f8a,#3aa3e0)"><div class="date">07.Aug.2016</div></div>
    <h3>Lorem ipsum dolor sit amet</h3>
    <p>Lorem ipsum dolor sit amet, consectetuer adipiscing elit, sed diam nonummy nibh euismod tincidunt ut laoreet dolore magna aliquam erat volutpat. Ut wisi enim ad minim...<em>[+]</em></p>
  </article>
  <article class="post" style="left:803px">
    <div class="thumb" role="img" aria-label="Photo of a padlock resting on a laptop keyboard" style="background:linear-gradient(160deg,#0b0b0b,#4a4a4a)"><div class="date">08.Aug.2016</div></div>
    <h3>Lorem ipsum dolor sit amet</h3>
    <p>Lorem ipsum dolor sit amet, consectetuer adipiscing elit, sed diam nonummy nibh euismod tincidunt ut laoreet dolore magna aliquam erat volutpat. Ut wisi enim ad minim...<em>[+]</em></p>
  </article>
</section>

<div class="cta">
  <p>Lorem ipsum dolor sit amet consectetuer adipiscing elit sed diam</p>
  <div class="btn-pill">Learn More</div>
</div>

<footer class="footer">
  <div class="fcol quick" style="left:101px;width:130px">
    <h4>Quick Links</h4>
    <ul><li>Home</li><li>About Us</li><li>Services</li><li>Blog</li><li>Contact Us</li></ul>
  </div>
  <div class="fcol contact" style="left:275px;width:240px">
    <h4>Contact Details</h4>
    <div class="row"><svg width="12" height="16" viewBox="0 0 12 16"><path d="M6 0a6 6 0 0 1 6 6c0 4-6 10-6 10S0 10 0 6a6 6 0 0 1 6-6z" fill="#abd036"/><circle cx="6" cy="6" r="2" fill="#333"/></svg><span>123 euismod cidun ut laoreet laore<br>dol magna aliquam Feugait.</span></div>
    <div class="row"><svg width="14" height="14" viewBox="0 0 24 24"><path fill="#abd036" d="M6.6 10.8a15 15 0 0 0 6.6 6.6l2.2-2.2c.3-.3.7-.4 1-.2 1.1.4 2.3.6 3.6.6.6 0 1 .4 1 1V20c0 .6-.4 1-1 1A17 17 0 0 1 3 4c0-.6.4-1 1-1h3.5c.6 0 1 .4 1 1 0 1.3.2 2.5.6 3.6.1.3 0 .7-.2 1z"/></svg><span>(555) 014 - 2290</span></div>
    <div class="row"><svg width="14" height="14" viewBox="0 0 14 14"><rect x="3" y="0" width="8" height="4" fill="#abd036"/><rect x="0" y="4" width="14" height="6" fill="#abd036"/><rect x="3" y="8" width="8" height="6" fill="#abd036" stroke="#333"/></svg><span>(555) 014 - 2290</span></div>
    <div class="row"><svg width="14" height="11" viewBox="0 0 14 11"><rect width="14" height="11" fill="#abd036"/><path d="M0 0l7 6 7-6" fill="none" stroke="#333"/></svg><span><b>info@brightquarry.com</b></span></div>
  </div>
  <div class="fcol form" style="left:569px;width:260px">
    <h4 style="width:230px">Quick Inquiry</h4>
    <div class="field">Name</div>
    <div class="field">Email</div>
    <div class="field msg">Message</div>
    <div class="send">Submit</div>
  </div>
  <div class="flogo">BrightQuarry</div>
  <div class="fsocial"><span></span><span></span><span></span><span></span></div>
</footer>
<div class="copy">Copyright © 2016 BrightQuarry. All Rights Reserved.</div>

</div>
</body>
</html>
```